KWI Business Card

Please create a creative design for a business card using the new theme from the Logo & website. This company's main focus is food manufacturing building construction. Please integrate the new logo attached.

Please use the following information for the demo card:

Korvel Walls, Inc.
Dana Whitcombe
dwhitcombe@korvelwalls.example
Cell: 312-555-0178
218 Larkmoor Ave
Ashgrove, KV 60418

See pictures and more information on the website.

www.korvelwalls.example

```html
<!DOCTYPE html>
<html lang="en">
<head>
<meta charset="utf-8">
<title>Korvel Walls, Inc. — Business Card</title>
<link rel="stylesheet" href="https://fonts.googleapis.com/css2?family=Red+Hat+Text:wght@400;500;700&display=swap">
<style>
  :root {
    --backdrop: #e2e2e2;
    --card-dark: #2b2a29;
    --card-light: #f4f4f4;
    --brand-blue: #1f6fb5;
    --logo-blue: #4a8fd0;
    --ink: #2b2a29;
    --text-on-dark: #d8d8d8;
    --rule: #3a3a3a;
  }
  * { margin: 0; padding: 0; box-sizing: border-box; }
  html, body {
    width: 1200px;
    height: 960px;
    overflow: hidden;
    background: var(--backdrop);
    font-family: "Red Hat Text", "Helvetica Neue", Arial, sans-serif;
  }
  .card {
    position: absolute;
    left: 315px;
    width: 568px;
    height: 325px;
  }
  .card--front { top: 130px; background: var(--card-dark); }
  .card--back  { top: 505px; background: var(--card-light); overflow: hidden; }

  .brand {
    position: absolute;
    display: flex;
    align-items: center;
    color: var(--logo-blue);
    font-weight: 700;
    white-space: nowrap;
  }
  .brand__square { background: var(--logo-blue); flex: none; }

  .card--front .brand {
    left: 0; right: 0; top: 150px;
    justify-content: center;
    gap: 14px;
    font-size: 34px;
  }
  .card--front .brand__square { width: 22px; height: 22px; }

  .front-web {
    position: absolute;
    left: 0; right: 0; top: 283px;
    text-align: center;
    font-size: 15px;
    letter-spacing: 1px;
    color: var(--text-on-dark);
  }
  .front-web .accent { color: var(--brand-blue); font-weight: 500; }

  .card--back .brand {
    left: 38px; top: 88px;
    gap: 9px;
    font-size: 19px;
  }
  .card--back .brand__square { width: 13px; height: 13px; }

  .person-name {
    position: absolute;
    right: 41px; top: 182px;
    font-size: 20px;
    font-weight: 700;
    letter-spacing: 0.3px;
    color: var(--brand-blue);
  }
  .divider {
    position: absolute;
    left: 40px; right: 41px; top: 217px;
    height: 1px;
    background: var(--rule);
  }
  .contacts {
    position: absolute;
    left: 42px; top: 231px;
    list-style: none;
    font-size: 15px;
    color: var(--ink);
    line-height: 19px;
  }
  .contacts li { display: flex; align-items: center; gap: 4px; }
  .contacts svg { width: 12px; height: 12px; flex: none; }
  .address {
    position: absolute;
    right: 41px; top: 250px;
    text-align: right;
    font-size: 15px;
    line-height: 19px;
    color: var(--ink);
    font-style: normal;
  }
  .footer-band {
    position: absolute;
    left: 0; bottom: 0;
    width: 568px; height: 14px;
  }
</style>
</head>
<body>
  <section class="card card--front" aria-label="Card front">
    <div class="brand">
      <span class="brand__square"></span>
      <span class="brand__name">Korvel Walls, Inc.</span>
    </div>
    <p class="front-web">www.<span class="accent">korvelwalls</span>.example</p>
  </section>

  <section class="card card--back" aria-label="Card back">
    <div class="brand">
      <span class="brand__square"></span>
      <span class="brand__name">Korvel Walls, Inc.</span>
    </div>

    <h1 class="person-name">DANA WHITCOMBE</h1>
    <div class="divider"></div>

    <ul class="contacts">
      <li>
        <svg viewBox="0 0 12 12" aria-hidden="true"><rect x="3" y="0.7" width="6" height="10.6" rx="1" fill="none" stroke="#1f6fb5" stroke-width="1.2"/><line x1="5" y1="9.4" x2="7" y2="9.4" stroke="#1f6fb5" stroke-width="1"/></svg>
        <span>312-555-0178</span>
      </li>
      <li>
        <svg viewBox="0 0 12 12" aria-hidden="true"><rect x="0.7" y="2.2" width="10.6" height="7.6" fill="none" stroke="#1f6fb5" stroke-width="1.2"/><path d="M0.9 2.6 L6 6.6 L11.1 2.6" fill="none" stroke="#1f6fb5" stroke-width="1.1"/></svg>
        <span>dwhitcombe@korvelwalls.example</span>
      </li>
      <li>
        <svg viewBox="0 0 12 12" aria-hidden="true"><circle cx="6" cy="6" r="5.2" fill="none" stroke="#1f6fb5" stroke-width="1.1"/><ellipse cx="6" cy="6" rx="2.3" ry="5.2" fill="none" stroke="#1f6fb5" stroke-width="1"/><line x1="0.8" y1="6" x2="11.2" y2="6" stroke="#1f6fb5" stroke-width="1"/></svg>
        <span>www.korvelwalls.example</span>
      </li>
    </ul>

    <address class="address">218 Larkmoor Ave<br>Ashgrove, KV 60418</address>

    <svg class="footer-band" viewBox="0 0 568 14" aria-hidden="true">
      <polygon points="0,0 361,0 353,14 0,14" fill="#2b2a29"/>
      <polygon points="366,0 568,0 568,14 358,14" fill="#1f6fb5"/>
    </svg>
  </section>
</body>
</html>
```